Bully breed rescue website

I need a website for my bully breed rescue. We rescue bully breeds from up and down the east coast of the United States and train them as service dogs for people with limited mobility disabilities. I don't want a lot of white space. I want it to be modern and slick and colorful and still look professional. I want it to be different and have a lot of wow factor. I linked a copy of my logo.

Number of Pages Required

5+ page

Font styles to use
Sans Serif

Colors

Designer to choose colors to be used in the design.

Requirements
Must have
• Moving aspects. Blog and ecommerce.
• 1.) Home page
• 2.) Services- something modular
• 3.) About US
• 4.) Blog
• 5.) Application page
• 6.) Donation page
• 7.) Contact Us
Nice to have
• Large Slider of photos on home page
• vertical menu bar
Should not have
• Lots of white space. Dont want it to look like a template or any other site

```html
<!DOCTYPE html>
<html lang="en">
<head>
<meta charset="utf-8">
<title>Quenbridge Paw Collective – Home</title>
<link href="https://fonts.googleapis.com/css2?family=Barlow:wght@500;600;700&family=Barlow+Condensed:wght@500;600&family=Open+Sans:wght@400;600;700&display=swap" rel="stylesheet">
<style>
  :root{
    --green:#2ecc8a;
    --ink:#0b0b0b;
    --paper:#f4f0ef;
    --white:#ffffff;
    --panel:rgba(60,70,80,.55);
    --field:rgba(235,235,235,.82);
  }
  *{box-sizing:border-box;margin:0;padding:0}
  html,body{width:675px;height:1200px;overflow:hidden;background:var(--white)}
  body{position:relative;font-family:"Open Sans",sans-serif;color:var(--ink)}
  .abs{position:absolute}

  /* hero */
  .hero{left:0;top:0;width:675px;height:378px;overflow:hidden;
    background:radial-gradient(ellipse at 40% 45%,#d9d2cc 0%,#b9aca3 30%,#8a7f7c 55%,#6d8294 80%,#4f6b80 100%)}
  .brand{left:22px;top:40px;display:flex;align-items:center;gap:8px}
  .brand-dot{width:14px;height:14px;border-radius:50%;background:var(--ink)}
  .brand-name{font-family:"Barlow",sans-serif;font-weight:700;font-size:14px;color:var(--ink);white-space:nowrap}

  .donate{left:476px;top:7px;width:188px;height:327px;background:var(--panel)}
  .donate-title{position:absolute;left:0;right:0;top:24px;text-align:center;
    font-family:"Barlow Condensed",sans-serif;font-weight:600;font-size:29px;color:#eee;letter-spacing:.5px}
  .field{position:absolute;left:16px;width:155px;height:33px;background:var(--field);
    font-size:10px;font-weight:600;letter-spacing:.6px;color:#333;padding:11px 0 0 5px}
  .donate-btn{position:absolute;left:16px;top:252px;width:155px;height:53px;
    background:linear-gradient(90deg,#4fbf9a,#7fd4b6);display:flex;align-items:center;justify-content:center;
    font-family:"Barlow Condensed",sans-serif;font-weight:600;font-size:29px;color:#eef;letter-spacing:.5px}

  .nav{left:0;top:333px;width:675px;height:28px}
  .nav a{position:absolute;top:0;height:28px;line-height:28px;font-size:14px;color:var(--white);
    text-decoration:none;letter-spacing:.3px;white-space:nowrap}
  .nav .current{left:90px;width:104px;background:var(--green);border-radius:14px;text-align:center}

  /* welcome */
  .welcome{left:0;top:378px;width:675px;height:193px;background:var(--paper)}
  .welcome h1{position:absolute;left:52px;top:30px;font-family:"Barlow",sans-serif;font-weight:700;font-size:29px;letter-spacing:1px}
  .welcome p{position:absolute;left:52px;top:68px;width:340px;font-size:9px;line-height:14px;font-weight:600;color:#222;white-space:nowrap}
  .pill{position:absolute;background:var(--green);color:var(--white);border-radius:14px;
    display:flex;align-items:center;justify-content:center;font-family:"Barlow",sans-serif;font-weight:600;white-space:nowrap}
  .welcome .pill{left:52px;top:136px;width:104px;height:28px;font-size:15px}
  .welcome-photo{position:absolute;left:394px;top:0;width:195px;height:193px;
    background:radial-gradient(ellipse at 50% 45%,#f3ece9 0%,#ead9d2 45%,#c99a83 75%,#efe8e6 100%)}

  /* slider */
  .slider{left:0;top:572px;width:675px;height:194px;background:var(--ink)}
  .slide-photo{position:absolute;left:272px;top:0;width:131px;height:194px;
    background:radial-gradient(ellipse at 50% 45%,#9a9a9a 0%,#4a4a4a 45%,#111 85%)}
  .arrow{position:absolute;top:82px;width:32px;height:32px}

  /* gallery */
  .gallery{left:0;top:766px;width:675px;height:237px;background:var(--white)}
  .tile{position:absolute}
  .gallery .pill{left:301px;top:175px;width:92px;height:26px;font-size:13px}

  /* contact */
  .contact{left:0;top:1003px;width:675px;height:197px;background:var(--ink);color:var(--white)}
  .contact h2{position:absolute;left:0;right:0;top:6px;text-align:center;font-family:"Barlow",sans-serif;font-weight:600;font-size:24px;line-height:28px;letter-spacing:.5px}
  .input{position:absolute;height:12px;border-bottom:1px solid var(--white);font-size:7px;font-weight:700;letter-spacing:.2px}
  .contact .pill{left:307px;top:104px;width:80px;height:22px;font-size:12px}
  .social{position:absolute;left:0;right:0;top:142px;display:flex;justify-content:center;gap:14px;
    font-family:"Barlow",sans-serif;font-weight:600;font-size:12px}
  .copyright{position:absolute;left:0;right:0;top:182px;text-align:center;font-size:5px;font-weight:600}
</style>
</head>
<body>

<header class="hero abs">
  <div class="abs" role="img" aria-label="Close-up photo of a smiling bulldog" style="inset:0"></div>
  <div class="brand abs"><span class="brand-dot"></span><span class="brand-name">Quenbridge Paw Collective</span></div>

  <form class="donate abs">
    <div class="donate-title">DONATE NOW</div>
    <div class="field" style="top:87px">FIRST NAME</div>
    <div class="field" style="top:125px">LAST NAME</div>
    <div class="field" style="top:162px">AMOUNT</div>
    <div class="field" style="top:200px">EMAIL ADDRESS</div>
    <div class="donate-btn">DONATE</div>
  </form>

  <nav class="nav abs">
    <a class="current">HOME</a>
    <a style="left:209px">SERVICES- SOMETHING MODULAR</a>
    <a style="left:459px">ABOUT US</a>
    <a style="left:549px">BLOG</a>
  </nav>
</header>

<section class="welcome abs">
  <h1>Welcome</h1>
  <p>We rescue bully breeds from up and down<br>the east coast of the United States and train them as service dogs for people,<br>with limited mobility disabilities.</p>
  <div class="pill">Learn more</div>
  <div class="welcome-photo" role="img" aria-label="Photo of a white bulldog puppy sitting"></div>
</section>

<section class="slider abs">
  <div class="slide-photo" role="img" aria-label="Black and white photo of a seated bulldog"></div>
  <svg class="arrow" style="left:53px" viewBox="0 0 32 32" aria-hidden="true">
    <circle cx="16" cy="16" r="14.5" fill="none" stroke="#777" stroke-width="2"/>
    <path d="M18.5 9 L11.5 16 L18.5 23" fill="none" stroke="#777" stroke-width="2"/>
  </svg>
  <svg class="arrow" style="left:597px" viewBox="0 0 32 32" aria-hidden="true">
    <circle cx="16" cy="16" r="14.5" fill="none" stroke="#777" stroke-width="2"/>
    <path d="M13.5 9 L20.5 16 L13.5 23" fill="none" stroke="#777" stroke-width="2"/>
  </svg>
</section>

<section class="gallery abs">
  <div class="tile" role="img" aria-label="Photo of a bulldog puppy lying on a bed" style="left:99px;top:30px;width:129px;height:166px;background:linear-gradient(160deg,#b9a796 0%,#8a6a52 45%,#c98d5c 70%,#e8e2d8 100%)"></div>
  <div class="tile" role="img" aria-label="Photo of a bulldog puppy walking on grass" style="left:266px;top:30px;width:161px;height:129px;background:linear-gradient(180deg,#5f7a3c 0%,#8c7a4f 45%,#b8733f 65%,#a59a5c 100%)"></div>
  <div class="tile" role="img" aria-label="Photo of a black pug" style="left:466px;top:30px;width:140px;height:166px;background:radial-gradient(ellipse at 45% 55%,#1c1a18 0%,#2c2a25 55%,#5b6a3a 100%)"></div>
  <div class="pill">Abous Us</div>
</section>

<footer class="contact abs">
  <h2>Contacts Us</h2>
  <div class="input" style="left:182px;top:40px;width:90px">YOUR NAME</div>
  <div class="input" style="left:301px;top:40px;width:90px">EMAIL</div>
  <div class="input" style="left:421px;top:40px;width:90px">PHONE</div>
  <div class="input" style="left:182px;top:75px;width:329px;border-bottom-width:2px">MESSAGE</div>
  <div class="pill">Email</div>
  <div class="social"><span>Pawgram</span><span>Barkbook</span><span>Yapper</span></div>
  <div class="copyright">Copyright 2018 - 2019. All Rights Reserved</div>
</footer>

</body>
</html>
```